Visitenkarten-Design für Ingenieurfirma
Zielgruppe
Wir sind eine Ingenieurfirma und planen Bauvorhaben - unsere Zielgruppe ist konservativ.
Aufgabenstellung
Schlichtes Design

```html
<!DOCTYPE html>
<html lang="de">
<head>
<meta charset="utf-8">
<title>bauvera – Visitenkarte</title>
<link rel="stylesheet" href="https://fonts.googleapis.com/css2?family=Exo+2:wght@300;400;500&display=swap">
<style>
  :root {
    --stage: #262626;
    --card-white: #ffffff;
    --card-dark: #3a3a3a;
    --band: #333333;
    --orange: #c77a3a;
    --grey-text: #6f6f6f;
    --light-text: #f2f2f2;
  }
  * { box-sizing: border-box; margin: 0; padding: 0; }
  html, body {
    width: 1200px; height: 801px; overflow: hidden;
    background: var(--stage);
    font-family: "Exo 2", sans-serif;
  }
  .stage {
    position: relative; width: 1200px; height: 801px;
    display: flex; align-items: center; justify-content: center; gap: 40px;
  }
  .card {
    position: relative; width: 520px; height: 336px;
    box-shadow: 0 12px 30px rgba(0,0,0,.45);
    overflow: hidden;
  }
  .card-front { background: var(--card-white); }
  .card-back { background: var(--card-dark); display: flex; align-items: center; justify-content: center; }

  .brand-name {
    color: var(--orange); font-weight: 400; line-height: 1;
    letter-spacing: 1px;
  }
  .front-brand { position: absolute; left: 44px; top: 56px; font-size: 64px; }
  .back-brand { font-size: 92px; letter-spacing: 3px; }

  .person { position: absolute; left: 44px; top: 196px; color: var(--grey-text); }
  .person-name { font-size: 19px; font-weight: 400; }
  .person-role { font-size: 15px; font-weight: 300; margin-top: 2px; }

  .contact {
    position: absolute; right: 34px; top: 52px;
    font-size: 12.5px; font-weight: 400; color: var(--grey-text);
    list-style: none; line-height: 1.55;
  }
  .contact-company { margin-bottom: 4px; font-size: 14px; }
  .contact-company .brand-name { letter-spacing: 0; }
  .contact li { display: flex; align-items: flex-start; gap: 8px; }
  .contact svg { flex: none; width: 12px; height: 12px; margin-top: 4px; fill: var(--orange); }
  .contact .no-icon { padding-left: 20px; }

  .web-band {
    position: absolute; left: 0; right: 0; bottom: 0; height: 58px;
    background: var(--band);
    display: flex; align-items: center; justify-content: flex-end; gap: 10px;
    padding-right: 34px; color: var(--light-text); font-size: 15px; font-weight: 300;
  }
  .web-band svg { width: 20px; height: 20px; stroke: var(--light-text); fill: none; stroke-width: 1.3; }
</style>
</head>
<body>
<main class="stage">
  <section class="card card-front" aria-label="Vorderseite">
    <div class="brand-name front-brand">bauvera</div>

    <div class="person">
      <p class="person-name">Name und Nachname</p>
      <p class="person-role">Manager</p>
    </div>

    <ul class="contact">
      <li class="contact-company"><span><span class="brand-name">bauvera</span> GmbH</span></li>
      <li>
        <svg viewBox="0 0 12 12" aria-hidden="true"><path d="M1 5 11 1 7 11 6 6Z"/></svg>
        <span>Lindenauer Weg 7</span>
      </li>
      <li class="no-icon">10115 Musterstadt</li>
      <li>
        <svg viewBox="0 0 12 12" aria-hidden="true"><path d="M2 1h3l1 3-2 1a7 7 0 0 0 3 3l1-2 3 1v3c-6 1-10-3-9-9Z"/></svg>
        <span>030/555 01 210</span>
      </li>
      <li>
        <svg viewBox="0 0 12 12" aria-hidden="true"><path d="M3 1h6v3H3ZM1 5h10v5H9V8H3v2H1ZM3 9h6v2H3Z"/></svg>
        <span>030/555 01 212</span>
      </li>
      <li>
        <svg viewBox="0 0 12 12" aria-hidden="true"><path d="M1 3h10v7H1Zm1 1 4 3 4-3Z"/></svg>
        <span>info@bauvera-test.de</span>
      </li>
    </ul>

    <div class="web-band">
      <svg viewBox="0 0 20 20" aria-hidden="true">
        <circle cx="10" cy="10" r="8"/>
        <ellipse cx="10" cy="10" rx="3.5" ry="8"/>
        <path d="M2 10h16M3.5 6h13M3.5 14h13"/>
      </svg>
      <span>www.bauvera-test.de</span>
    </div>
  </section>

  <section class="card card-back" aria-label="Rückseite">
    <div class="brand-name back-brand">bauvera</div>
  </section>
</main>
</body>
</html>
```